Brava Stone Oven Kitchen (restaurant)

Restaurant with a cool vibe.
We need a refresh of existing site. Appealing to a hip crowd of 25 or older age bracket (mid price to high small town). Constant changes food and cocktail menu. A vibing atmosphere with jazz funk hip music.
Must be able to scale for any device… phone/mobile device super important.
Instagram: @Brava.Linwell
Website: bravalinwell.example

Target Market(s)

25-55 age group

Number of Pages Required

1 page

Font styles to use
Sans Serif

Requirements
Must have
• Simple to navigate. Simplicity is the key to all sophistication.

Links/Buttons
Menu
Gift Cards
Reservations
Take Out
Contact Us
Should not have
• Please, nothing generic looking… no cookie cutter look. Originality

```html
<!DOCTYPE html>
<html lang="en">
<head>
<meta charset="utf-8">
<title>Brava Stone Oven Kitchen</title>
<link href="https://fonts.googleapis.com/css2?family=Caveat+Brush&family=Roboto:wght@400;500;700&display=swap" rel="stylesheet">
<style>
:root{
  --orange:#c0570f;
  --orange-dark:#a84a0b;
  --brown:#2b1909;
  --brown-mid:#4a2c12;
  --ink:#1d1d1d;
  --paper:#ffffff;
  --mist:#f2f2f2;
  --line:#d9d9d9;
}
*{box-sizing:border-box;margin:0;padding:0}
html,body{width:1200px;height:3134px;overflow:hidden}
body{position:relative;background:var(--paper);font-family:"Roboto",Arial,sans-serif;color:var(--ink)}
.abs{position:absolute}
.script{font-family:"Caveat Brush",cursive;color:var(--orange);font-weight:400}
.section-title{position:absolute;left:0;width:1200px;text-align:center;font-size:40px;line-height:48px}

/* hero */
.hero{left:0;top:0;width:1200px;height:560px;background:
  radial-gradient(ellipse 420px 300px at 960px 330px,rgba(190,140,90,.55),transparent 70%),
  radial-gradient(ellipse 380px 260px at 720px 120px,rgba(170,120,70,.45),transparent 70%),
  linear-gradient(100deg,#3b2417 0%,#50301f 40%,#6a4a30 65%,#5a3d28 100%)}
.hero-shade{left:0;top:0;width:1200px;height:560px;background:rgba(0,0,0,.32)}
.brand{left:88px;top:30px;width:190px;color:var(--paper);font-weight:700;font-size:20px;line-height:22px;letter-spacing:.3px}
.nav{top:34px;left:477px;display:flex;gap:27px;font-size:13.5px;line-height:18px;color:var(--paper)}
.nav .active{color:var(--orange)}
.social{top:35px;left:1026px;display:flex;gap:17px}
.social span{width:16px;height:16px;border-radius:50%;display:block}
.hero-title{left:0;top:206px;width:1200px;text-align:center;color:var(--paper);font-family:"Caveat Brush",cursive;font-size:54px;line-height:64px}
.btn{display:inline-flex;align-items:center;justify-content:center;background:var(--orange);color:var(--paper);font-size:14.5px;border-radius:3px}
.hero-btn-1{left:449px;top:288px;width:147px;height:38px}
.hero-btn-2{left:604px;top:288px;width:147px;height:38px;border:2px solid var(--paper)}
.dots{left:541px;top:464px;display:flex;gap:14px}
.dots span{width:12px;height:12px;border:1.5px solid var(--paper);border-radius:50%;display:block}
.dots .on{background:radial-gradient(var(--paper) 40%,transparent 45%)}

/* menu */
.menu-card{top:678px;width:446px;height:268px;border:5px solid var(--paper);box-shadow:0 0 0 1px #e5e5e5}
.menu-card .photo{width:100%;height:100%}
.menu-card .dim{position:absolute;inset:0;background:rgba(0,0,0,.18)}
.menu-label{position:absolute;left:50%;top:50%;transform:translate(-50%,-50%);background:var(--paper);outline:2px solid var(--orange);outline-offset:-6px;color:var(--orange);font-weight:500;font-size:27px;line-height:32px;padding:21px 40px;white-space:nowrap}

/* gift */
.gift{left:0;top:1043px;width:1200px;height:390px;background:
  radial-gradient(ellipse 500px 200px at 400px 130px,rgba(120,80,45,.5),transparent 70%),
  radial-gradient(ellipse 420px 180px at 260px 330px,rgba(110,70,35,.45),transparent 70%),
  linear-gradient(120deg,#3a2311,#2c190a 60%,#3a2413)}
.gift-title{left:198px;top:1164px;font-size:38px;line-height:44px}
.gift-text{left:198px;top:1222px;width:540px;color:var(--paper);font-size:14.5px;line-height:22px}
.gift-text a{color:var(--orange)}
.gift-card{left:788px;top:1166px;width:240px;height:141px;border-radius:8px;background:linear-gradient(135deg,#f6f6f6,#dedede)}

/* reservations */
.reserve{left:0;top:1433px;width:1200px;height:362px;background:var(--mist)}
.reserve-head{left:0;top:1562px;width:1200px;text-align:center;font-size:19px;line-height:24px;font-weight:500}
.reserve-note{left:0;top:1590px;width:1200px;text-align:center;font-size:14.5px;line-height:20px}
.field{top:1673px;width:193px;height:42px;background:var(--paper);border:1px solid var(--line);display:flex;align-items:center;padding:0 18px;font-size:13px;color:#888;gap:10px}
.field .chev{margin-left:auto;width:18px;height:18px;border:1px solid #bbb;border-radius:2px;display:flex;align-items:center;justify-content:center}
.find-btn{left:833px;top:1673px;width:193px;height:42px;font-size:13.5px}

/* photos */
.view-btn{left:528px;top:2515px;width:145px;height:38px;font-size:13.5px}

/* footer */
.footer{left:0;top:2632px;width:1200px;height:466px;background:
  radial-gradient(ellipse 400px 160px at 420px 330px,rgba(90,55,25,.45),transparent 70%),
  linear-gradient(180deg,#2e1b0a,#241506)}
.contact{top:2720px;display:flex;gap:10px;align-items:center;color:var(--paper)}
.contact .ring{width:50px;height:50px;border-radius:50%;border:2px solid var(--orange);display:flex;align-items:center;justify-content:center}
.contact .ring i{width:38px;height:38px;border-radius:50%;background:var(--orange);display:flex;align-items:center;justify-content:center}
.contact small{display:block;color:var(--orange);font-size:13px;line-height:16px}
.contact b{font-weight:400;font-size:14.5px;line-height:18px}
.hours{top:2832px;color:var(--paper);font-size:13px;line-height:24px}
.hours h3{font-family:"Caveat Brush",cursive;color:var(--orange);font-weight:400;font-size:22px;margin-bottom:8px;line-height:28px}
.map{left:848px;top:2828px;width:263px;height:140px;border-radius:3px;background:linear-gradient(135deg,#eef0f2,#dde3ea)}
.foot-nav{left:332px;top:3046px;display:flex;gap:41px;color:var(--paper);font-size:13.5px;line-height:18px}
.foot-nav .active{color:var(--orange);text-decoration:underline}
.copy-bar{left:0;top:3097px;width:1200px;height:37px;background:var(--orange);color:var(--paper);font-size:11.5px;display:flex;align-items:center;padding-left:88px}
.copy-social{left:1016px;top:3110px;display:flex;gap:16px}
.copy-social span{width:13px;height:13px;border-radius:50%;background:var(--paper);display:block}
</style>
</head>
<body>

<!-- hero -->
<div class="abs hero" role="img" aria-label="Photo of the brick restaurant front beside wood fired pizzas"></div>
<div class="abs hero-shade"></div>
<div class="abs brand">Brava Stone Oven Kitchen</div>
<nav class="abs nav">
  <span class="active">Home</span><span>Menu</span><span>Gift Cards</span><span>Reservations</span><span>Take Out</span><span>Contact Us</span>
</nav>
<div class="abs social"><span style="background:var(--orange)"></span><span style="background:var(--orange)"></span><span style="background:var(--paper)"></span></div>
<div class="abs hero-title">Lets Get Lunch At Brava!</div>
<div class="abs btn hero-btn-1">Order Online</div>
<div class="abs btn hero-btn-2">Book A Table</div>
<div class="abs dots"><span></span><span class="on"></span><span></span><span></span><span></span></div>
<svg class="abs" style="left:0;top:500px" width="1200" height="70" viewBox="0 0 1200 70">
  <path d="M0 52 L120 44 L300 38 L390 30 L520 26 L640 32 L760 28 L900 36 L1040 46 L1200 48 L1200 70 L0 70Z" fill="var(--paper)"/>
  <path d="M380 28 L560 20 L700 24 L560 28Z M1100 48 L1200 40 L1200 46Z" fill="var(--paper)"/>
</svg>

<!-- menu -->
<h2 class="section-title script" style="top:602px">Our Menu</h2>
<div class="abs menu-card" style="left:143px">
  <div class="photo" role="img" aria-label="Photo of tacos with red cabbage and greens" style="background:radial-gradient(ellipse 160px 110px at 320px 80px,#8a4f8a,transparent 70%),radial-gradient(ellipse 150px 100px at 110px 200px,#6a3a22,transparent 70%),linear-gradient(135deg,#5a3a2a,#7b4a6a 45%,#8a6a3a)"></div>
  <div class="dim"></div>
  <div class="menu-label">Dinner</div>
</div>
<div class="abs menu-card" style="left:616px">
  <div class="photo" role="img" aria-label="Photo of a sandwich with greens" style="background:radial-gradient(ellipse 200px 90px at 220px 70px,#8a6440,transparent 70%),linear-gradient(135deg,#3e2c22,#6a4a36 50%,#3a3a28)"></div>
  <div class="dim"></div>
  <div class="menu-label">Take Out</div>
</div>

<!-- gift cards -->
<div class="abs gift" role="img" aria-label="Dim photo of a pizza on a wooden board"></div>
<svg class="abs" style="left:0;top:1038px" width="1200" height="30" viewBox="0 0 1200 30">
  <path d="M0 0 L1200 0 L1200 5 L1000 12 L760 8 L560 18 L400 10 L200 14 L0 8Z" fill="var(--paper)"/>
</svg>
<h2 class="abs gift-title script">Gift Cards</h2>
<p class="abs gift-text">Lorem Ipsum is simply dummy text of the printing and typesetting industry. Lorem Ipsum has been the industry's standard dummy text ever since the 1500s, when an unknown. <a href="#">more</a></p>
<div class="abs gift-card" role="img" aria-label="Gift card with a red ribbon bow and the restaurant name"></div>
<svg class="abs" style="left:0;top:1405px" width="1200" height="30" viewBox="0 0 1200 30">
  <path d="M0 22 L180 16 L400 20 L600 12 L820 18 L1000 14 L1200 20 L1200 30 L0 30Z" fill="var(--mist)"/>
</svg>

<!-- reservations -->
<div class="abs reserve"></div>
<h2 class="section-title script" style="top:1494px">Reservations</h2>
<div class="abs reserve-head">Reservations are not currently available</div>
<div class="abs reserve-note">Reservations will not be available for the courtyard under phase 1 and 2 of reopening. Walk-ins only.<br>We can't wait to see you!</div>
<div class="abs field" style="left:182px">
  <svg width="16" height="16" viewBox="0 0 16 16"><rect x="1.5" y="3" width="13" height="11.5" rx="1" fill="none" stroke="var(--orange)" stroke-width="1.5"/><path d="M1.5 6.5h13M5 1v3M11 1v3" stroke="var(--orange)" stroke-width="1.5"/></svg>
  Date<span class="chev"><svg width="10" height="6"><path d="M1 1l4 4 4-4" fill="none" stroke="var(--orange)" stroke-width="1.5"/></svg></span>
</div>
<div class="abs field" style="left:399px">
  <svg width="16" height="16" viewBox="0 0 16 16"><circle cx="8" cy="8" r="6.5" fill="none" stroke="var(--orange)" stroke-width="1.5"/><path d="M8 4v4l3 2" fill="none" stroke="var(--orange)" stroke-width="1.5"/></svg>
  Time<span class="chev"><svg width="10" height="6"><path d="M1 1l4 4 4-4" fill="none" stroke="var(--orange)" stroke-width="1.5"/></svg></span>
</div>
<div class="abs field" style="left:615px">
  <svg width="16" height="16" viewBox="0 0 16 16"><circle cx="8" cy="5" r="3.3" fill="none" stroke="var(--orange)" stroke-width="1.5"/><path d="M2 15c0-3.5 2.7-5.5 6-5.5s6 2 6 5.5" fill="none" stroke="var(--orange)" stroke-width="1.5"/></svg>
  Party Size<span class="chev"><svg width="10" height="6"><path d="M1 1l4 4 4-4" fill="none" stroke="var(--orange)" stroke-width="1.5"/></svg></span>
</div>
<div class="abs btn find-btn">Find a Table</div>

<!-- photos -->
<h2 class="section-title script" style="top:1868px">Our Photos</h2>
<div class="abs" style="left:89px;top:1954px;width:374px;height:259px;background:radial-gradient(ellipse 150px 120px at 200px 150px,#8a7060,transparent 70%),linear-gradient(135deg,#4a4440,#7a6a5a)" role="img" aria-label="Photo of the restaurant team by the oven"></div>
<div class="abs" style="left:464px;top:1954px;width:373px;height:259px;background:radial-gradient(ellipse 170px 110px at 190px 150px,#c8883e,transparent 75%),radial-gradient(ellipse 90px 60px at 200px 130px,#5e7a2e,transparent 70%),linear-gradient(135deg,#3a2e26,#5a4230)" role="img" aria-label="Photo of a pizza topped with arugula"></div>
<div class="abs" style="left:838px;top:1954px;width:272px;height:259px;background:radial-gradient(ellipse 110px 110px at 120px 130px,#e0bc6a,transparent 75%),linear-gradient(135deg,#7a5a3a,#a8865a)" role="img" aria-label="Photo of a pressed ham and cheese sandwich with pickles"></div>
<div class="abs" style="left:89px;top:2215px;width:374px;height:258px;background:radial-gradient(ellipse 160px 70px at 170px 80px,#d8cfc0,transparent 75%),radial-gradient(ellipse 140px 80px at 260px 190px,#3e5a24,transparent 75%),linear-gradient(135deg,#5a4a3a,#a0502a)" role="img" aria-label="Photo of grilled chicken over a salad"></div>
<div class="abs" style="left:464px;top:2215px;width:272px;height:258px;background:radial-gradient(ellipse 130px 70px at 140px 200px,#f2ece4,transparent 75%),linear-gradient(135deg,#6a5040,#c8a080)" role="img" aria-label="Photo of a server presenting tacos"></div>
<div class="abs" style="left:738px;top:2215px;width:372px;height:258px;background:radial-gradient(ellipse 150px 110px at 120px 90px,#d8b078,transparent 75%),radial-gradient(ellipse 140px 90px at 280px 200px,#a8502e,transparent 75%),linear-gradient(135deg,#8a6a48,#5a3a20)" role="img" aria-label="Photo of two wood fired pizzas"></div>
<div class="abs btn view-btn">View More</div>

<!-- footer -->
<div class="abs footer" role="img" aria-label="Dim photo of the brick building front"></div>
<svg class="abs" style="left:0;top:2625px" width="1200" height="40" viewBox="0 0 1200 40">
  <path d="M0 0 L1200 0 L1200 6 L1000 14 L760 10 L560 20 L340 12 L160 18 L0 10Z" fill="var(--paper)"/>
</svg>

<div class="abs contact" style="left:164px">
  <span class="ring"><i><svg width="18" height="18" viewBox="0 0 24 24"><path d="M6.6 10.8a15 15 0 006.6 6.6l2.2-2.2c.3-.3.7-.4 1-.2 1.1.4 2.3.6 3.6.6.6 0 1 .4 1 1V20c0 .6-.4 1-1 1A17 17 0 013 4c0-.6.4-1 1-1h3.5c.6 0 1 .4 1 1 0 1.2.2 2.4.6 3.6.1.3 0 .7-.2 1z" fill="var(--paper)"/></svg></i></span>
  <div><small>Phone</small><b>555-204-1187</b></div>
</div>
<div class="abs contact" style="left:375px">
  <span class="ring"><i><svg width="18" height="14" viewBox="0 0 18 14"><rect x="0" y="0" width="18" height="14" rx="1.5" fill="var(--paper)"/><path d="M1 1l8 6 8-6" fill="none" stroke="var(--orange)" stroke-width="1.6"/></svg></i></span>
  <div><small>Email</small><b>hello@bravalinwell.example</b></div>
</div>
<div class="abs contact" style="left:675px">
  <span class="ring"><i><svg width="14" height="19" viewBox="0 0 14 19"><path d="M7 0a7 7 0 017 7c0 5-7 12-7 12S0 12 0 7a7 7 0 017-7z" fill="var(--paper)"/><circle cx="7" cy="7" r="2.6" fill="var(--orange)"/></svg></i></span>
  <div><small>Address</small><b>48 Mill Row Street &nbsp;|&nbsp; Linwell, ON &nbsp;|&nbsp; K0L 2B4</b></div>
</div>

<div class="abs hours" style="left:88px">
  <h3>Canada Day Hours!</h3>
  Thursday, July 1st &nbsp;- &nbsp;Open<br>Friday, July 2nd &nbsp;- &nbsp;Open<br>Saturday, July 3rd &nbsp;- &nbsp;Open<br>Sunday, July 4th &nbsp;- &nbsp;Closed
</div>
<div class="abs hours" style="left:353px">
  <h3>Pickup &amp; Kitchen Hours</h3>
  Thursday to Sunday<br>12:00pm – 8:00pm
</div>
<div class="abs hours" style="left:617px">
  <h3>Dining Hours</h3>
  Courtyard is open<br>Thursday to Sunday<br>12:00pm – 9:00pm
</div>
<div class="abs map" role="img" aria-label="Street map showing the restaurant location"></div>

<nav class="abs foot-nav">
  <span class="active">Home</span><span>Menu</span><span>Gift Cards</span><span>Reservations</span><span>Take Out</span><span>Contact Us</span>
</nav>
<div class="abs copy-bar">Copyright © 2021 Bravalinwell. All Rights Reserved</div>
<div class="abs copy-social"><span></span><span></span><span></span></div>

</body>
</html>
```